DOVR Business Card Design Project

Company Name: DOVR (Dove Operational Versatile Resources) JLT.
Office Address: Office No 218, Saffron Crest Tower, Palmera Bay Towers, Dubai, U.A.E
Company line of business:
1) Currently we have a POS solution for retail outlets like duty free shops, supermarkets, department stores etc... The solution is deployed in Harbor Gate Retail on 350 POS and in Coralline Port Retail on 100 POS. So our main line of business is the deployment of this solution in retail outlets locally or regionally. We have already deployed the solution in India and Australia.
2) Integration of other third party POS systems with an online credit authorization netwotk in the UAE. This will enable POS applications to connect directly to the acquiring banks without needing an EFT terminal like Paxoline or Tramodex. The credit card payment is completed at the POS.
3) Other solutions that are targeting retail outlets like mobile POS, queue busting solutions, stock taking solutions using hand held devices, transaction capture systems, etc...
4) Other IT services like support of call center solutions from Bramwell Systems and development of new solutions as per customer requirements.
We need a business card design for the company. We don't have any specific requirements and will eave up to the designers to come up with creative designs. At the moment we still don't have a letter head design and the only thing that we have is the company logo that we will upload shortly.
Updates
Dear All,
I just uploaded the logo source files. I am sorry for the delay.
Regards
Tarek Demirci
I would like the business cards to have the following details:
Company Tel No
Company Fax No
Company Website Address
Employee Name
Employee Title
Employee Mobile Number
Employee Email Address

```html
<!DOCTYPE html>
<html lang="en">
<head>
<meta charset="utf-8">
<title>DOVR Business Card</title>
<link rel="stylesheet" href="https://fonts.googleapis.com/css2?family=Saira:wght@400;500&display=swap">
<style>
  :root {
    --backdrop: #ececec;
    --card: #ffffff;
    --brand-red: #e3202a;
    --brand-blue: #0a7ec2;
    --ink: #333333;
    --label: #1a86c8;
    --rule: #555555;
  }
  * { margin: 0; padding: 0; box-sizing: border-box; }
  html, body {
    width: 1200px;
    height: 900px;
    overflow: hidden;
    background: var(--backdrop);
    font-family: "Saira", Arial, sans-serif;
    color: var(--ink);
  }
  .canvas { position: relative; width: 1200px; height: 900px; }

  .card {
    position: absolute;
    width: 532px;
    height: 296px;
    background: var(--card);
  }
  .card--front { left: 139px; top: 112px; }
  .card--back  { left: 519px; top: 483px; }

  .band { position: absolute; left: 0; width: 100%; height: 13px; }
  .band--top { top: 0; background: var(--brand-red); }
  .band--bottom { bottom: 0; background: var(--brand-blue); }
  .tab { position: absolute; left: 82px; width: 194px; height: 26px; }
  .tab--top { top: 0; background: var(--brand-red); }
  .tab--bottom { bottom: 0; background: var(--brand-blue); }

  .brand {
    position: absolute;
    left: 0; right: 0; top: 108px;
    display: flex;
    align-items: center;
    justify-content: center;
    gap: 18px;
  }
  .brand__dot {
    width: 58px; height: 58px;
    border-radius: 50%;
    background: var(--brand-blue);
  }
  .brand__name {
    font-size: 64px;
    font-weight: 400;
    line-height: 1;
    letter-spacing: 2px;
    color: var(--ink);
  }

  .company {
    position: absolute;
    right: 271px;
    top: 88px;
    text-align: right;
  }
  .company__name {
    font-size: 16px;
    line-height: 21px;
    letter-spacing: 1.4px;
    margin-bottom: 14px;
  }
  .contact-line { font-size: 15.5px; line-height: 20px; }
  .contact-line .label { color: var(--label); }
  .contact-line--web { color: var(--label); }

  .divider {
    position: absolute;
    left: 276px;
    top: 79px;
    width: 2px;
    height: 138px;
    background: var(--rule);
  }

  .person { position: absolute; left: 292px; top: 84px; }
  .person__name { font-size: 25px; line-height: 30px; font-weight: 400; }
  .person__title { font-size: 15px; line-height: 18px; margin-bottom: 16px; }
</style>
</head>
<body>
<main class="canvas">
  <section class="card card--front" aria-label="Business card front">
    <div class="band band--top"></div>
    <div class="tab tab--top"></div>
    <div class="brand">
      <span class="brand__dot"></span>
      <span class="brand__name">DOVR</span>
    </div>
    <div class="tab tab--bottom"></div>
    <div class="band band--bottom"></div>
  </section>

  <section class="card card--back" aria-label="Business card back">
    <div class="band band--top"></div>
    <div class="tab tab--top"></div>

    <div class="company">
      <p class="company__name">Dove Operational<br>Versatile Resources PBT</p>
      <p class="contact-line"><span class="label">tel.:</span> +31 640 27 58</p>
      <p class="contact-line"><span class="label">fax:</span> +31 640 27 58</p>
      <p class="contact-line contact-line--web">www.dovr.com</p>
    </div>

    <div class="divider"></div>

    <div class="person">
      <h1 class="person__name">Mira Lindqvist</h1>
      <p class="person__title">manager</p>
      <p class="contact-line"><span class="label">tel.:</span> +31 640 27 58</p>
      <p class="contact-line"><span class="label">e–mail:</span> lindqvist@postmark.net</p>
    </div>

    <div class="tab tab--bottom"></div>
    <div class="band band--bottom"></div>
  </section>
</main>
</body>
</html>
```